Easy Marinade Labels for Butchery Store

Need a set of labels designed for a Butchery Shop. They will sit in the top left corner of the packets as a triangle (7cm each side). Easy because the only major requirement is the label name and some small text saying "Please ask in store to see spec sheet for ingredients". Extra points for finding a fun way to incorporate the logo and/or images of food (garlic bulbs, chilli, spices ect) to enhance the label. List of Marinade Names below: GarlicPepper Mint & RosemarySatayBBQChilli Plum & GingerSundried Tomato & BasilBuffaloHoney SoyHoi-SinPer PeriSpicy CajunTeriyakiBlack Bean Ive also attached the logo and an example of how the label might sit on a packet of meat. Thanks

Target Market(s)

Butchery Deli Shop Customers

Industry/Entity Type

Food Store

Font styles to use
Serif
Sans Serif
Decorative
Other font styles liked:
• Fun font that isn't a generic Quanderel Font?

Colors

Designer to choose colors to be used in the design.

Requirements
Must have
• Product Name
• Small text saying "Please ask in store to see spec sheet for ingredients"
Nice to have
• Photos of ingredients that would match that type of marinade - Chilli, Garlic, Spices.
• Brava Vell Logo - not essential if it doesn't look good on the label / doesn't fit.

```html
<!DOCTYPE html>
<html lang="en">
<head>
<meta charset="utf-8">
<title>Brava Vell – Marinade Label</title>
<link rel="stylesheet" href="https://fonts.googleapis.com/css2?family=Barlow+Condensed:wght@700&display=swap">
<style>
  :root {
    --paper: #ffffff;
    --slate-dark: #0e1214;
    --slate-mid: #2c3b3f;
    --slate-light: #4c6266;
    --label-text: #ffffff;
  }
  html, body {
    margin: 0;
    padding: 0;
    width: 1200px;
    height: 1200px;
    overflow: hidden;
    background: var(--paper);
  }
  .label {
    position: relative;
    width: 1200px;
    height: 1200px;
    background: var(--paper);
    overflow: hidden;
    font-family: "Barlow Condensed", "Arial Narrow", sans-serif;
    font-weight: 700;
    color: var(--label-text);
    text-transform: uppercase;
  }
  .ingredient-photo {
    position: absolute;
    inset: 0;
    clip-path: polygon(0 0, 100% 0, 0 100%);
    background:
      radial-gradient(ellipse 260px 120px at 330px 560px, rgba(180, 20, 20, 0.85), rgba(180, 20, 20, 0) 70%),
      radial-gradient(ellipse 110px 110px at 420px 320px, rgba(140, 120, 100, 0.7), rgba(140, 120, 100, 0) 70%),
      radial-gradient(ellipse 80px 60px at 500px 140px, rgba(110, 190, 50, 0.7), rgba(110, 190, 50, 0) 70%),
      linear-gradient(135deg, var(--slate-light) 0%, var(--slate-mid) 40%, var(--slate-dark) 85%);
  }
  .diagonal-text {
    position: absolute;
    transform-origin: 0 100%;
    transform: rotate(-45deg);
    white-space: nowrap;
    line-height: 1;
  }
  .product-name {
    left: 50px;
    top: 820px;
    font-size: 112px;
    letter-spacing: 4px;
  }
  .ingredient-note {
    left: 124px;
    top: 938px;
    font-size: 50px;
    letter-spacing: 1px;
  }
</style>
</head>
<body>
  <main class="label">
    <div class="ingredient-photo" role="img" aria-label="Photo of a red chilli, a garlic bulb and fresh basil leaves on a dark slate surface"></div>
    <h1 class="diagonal-text product-name" style="margin:0;">Brava Vell</h1>
    <p class="diagonal-text ingredient-note" style="margin:0;">Please ask in store to see spec sheet for ingredients</p>
  </main>
</body>
</html>
```